Still Harbor Weekend book cover design

I have attached an image that I would like this front cover to be similar to. This is a book about marriage so there will need to be a man and woman on the front cover and I am open to your creative design from that point. I have also attached the ISBN barcode and photo of authors for back cover. Book details are below:

Title:
Still HARBOR WEEKEND
Tending Covenant
A Workbook for the Shared Home and Kin

Authors: LEON AND TASHA’ MORVILLE
Book size : 8x10
Back cover text:
LEON AND TASHA’ MORVILLE

Authors, parents, grandparents, business owners, and public speakers, has served in ministry for over 25 years. They are the founders of Rise Forth Global Fellowship, serving as the senior pastors. They are also currently serving as national and international mission directors. They both are very intentional about assisting couples in developing their marriages. Having firsthand knowledge of God’s mercy in this area, the Morvilles are sharing the power of tending covenant with dedication and simplicity.

They are blessed to have three married children, and thirteen grandchildren in their more than 40 years of marriage. They are currently residing in Birmingham, Alabama. They look forward seeing you soon.

Back cover photo: Attached

```html
<!DOCTYPE html>
<html lang="en">
<head>
<meta charset="utf-8">
<title>Still Harbor Weekend — Book Cover</title>
<link href="https://fonts.googleapis.com/css2?family=Cinzel:wght@400;600&family=Lato:wght@300;400&family=EB+Garamond:ital,wght@1,600&display=swap" rel="stylesheet">
<style>
  :root {
    --paper: #ffffff;
    --ink: #2b2b2b;
    --accent: #c9785a;
    --art-peach: #f2b08a;
    --art-blush: #f6d9d2;
    --art-skin: #b8714f;
  }
  html, body {
    margin: 0;
    padding: 0;
    overflow: hidden;
    background: var(--paper);
  }
  .cover {
    position: relative;
    width: 960px;
    height: 1200px;
    background: var(--paper);
    overflow: hidden;
    color: var(--ink);
  }
  .cover h1 {
    margin: 0;
  }
  .series-word {
    position: absolute;
    top: 112px;
    left: 0;
    width: 100%;
    text-align: center;
    font-family: "Lato", sans-serif;
    font-weight: 400;
    font-size: 23px;
    letter-spacing: 3px;
    text-transform: uppercase;
    color: var(--accent);
  }
  .title {
    position: absolute;
    top: 158px;
    left: 0;
    width: 100%;
    margin: 0;
    font-weight: 400;
  }
  .title-line {
    display: block;
    width: 100%;
    text-align: center;
    font-family: "Cinzel", serif;
    font-weight: 400;
    font-size: 100px;
    line-height: 120px;
    height: 120px;
    text-transform: uppercase;
    color: var(--ink);
    box-sizing: border-box;
    white-space: nowrap;
  }
  .title-line--first {
    letter-spacing: 22px;
    padding-left: 22px;
  }
  .title-line--second {
    letter-spacing: 18px;
    padding-left: 18px;
  }
  .subtitle {
    position: absolute;
    top: 403px;
    left: 0;
    width: 100%;
    text-align: center;
    font-family: "Lato", sans-serif;
    font-weight: 400;
    font-size: 25px;
    letter-spacing: 4px;
    text-transform: uppercase;
    color: var(--ink);
  }
  .cover-art {
    position: absolute;
    left: 216px;
    top: 472px;
    width: 552px;
    height: 528px;
    border-radius: 40% 40% 12% 12%;
    background:
      radial-gradient(ellipse at 45% 25%, var(--art-skin) 0%, rgba(184,113,79,0) 35%),
      radial-gradient(ellipse at 30% 60%, var(--art-peach) 0%, rgba(242,176,138,0) 45%),
      radial-gradient(ellipse at 70% 60%, var(--art-blush) 0%, rgba(246,217,210,0) 50%),
      linear-gradient(180deg, #fbf1ec 0%, #f7e3da 60%, #ffffff 100%);
  }
  .tagline {
    position: absolute;
    top: 1036px;
    left: 0;
    width: 100%;
    text-align: center;
    font-family: "EB Garamond", serif;
    font-style: italic;
    font-weight: 600;
    font-size: 27px;
    color: var(--ink);
  }
  .authors {
    position: absolute;
    top: 1096px;
    left: 0;
    width: 100%;
    text-align: center;
    font-family: "Cinzel", serif;
    font-weight: 600;
    font-size: 34px;
    letter-spacing: 2.5px;
    color: #111111;
  }
</style>
</head>
<body>
  <main class="cover">
    <div class="series-word">Still</div>
    <h1 class="title">
      <span class="title-line title-line--first">HARBOR</span>
      <span class="title-line title-line--second">WEEKEND</span>
    </h1>
    <div class="subtitle">Tending Covenant</div>

    <div class="cover-art" role="img" aria-label="Illustration of a couple seated on two flower-decorated wedding chairs, embracing, with scattered petals"></div>

    <div class="tagline">A Workbook for the Shared Home and Kin</div>
    <div class="authors">LEON AND TASHA’ MORVILLE</div>
  </main>
</body>
</html>
```